Online Media Company Website

Looking for a website design that clearly and powerfully portrays our brand. Brookvane. We are an online media technology company that helps advertisers understand the content and verify the context where they advertise in online video.

You can see more about our company at www.brookvane.tv and watch the video. The only thing you must keep is the logo (attached). Everything else is fair game.

We need the following sections:

Home
About Us
-Company
-Careers
-Management
Technology
-Publisher Solutions
-Advertiser Solutions
Press
Contact Us

On the main page should be a space where we can place our video plus showcase some important news such as whitepapers..etc.

Please include social media functions on the homepage such as twitter/facebook. Perhaps a section for a twitter feed.

Sites we like:
www.glintaro.com
www.fernmingle.com
www.quaverclip.com
www.zenotap.com

Industry/Entity Type

Tv

Requirements
Nice to have
• social media feed

```html
<!DOCTYPE html>
<html lang="en">
<head>
<meta charset="utf-8">
<title>Brookvane — Online media technology company</title>
<link rel="stylesheet" href="https://fonts.googleapis.com/css2?family=Source+Sans+3:wght@400;600;700&display=swap">
<style>
:root{
  --brand:#2a8a9c;
  --ink:#1f1f1f;
  --blue:#148bd0;
  --blue-dark:#0a66a6;
  --pill:#1479c4;
  --band:#f3f3f3;
  --page:#e9e9e9;
  --rule:#b9b9b9;
  --muted:#6d6d6d;
  --heading:#3d3d3d;
  --footer:#3b3b3b;
  --footer-text:#dcdcdc;
  --white:#ffffff;
}
*{margin:0;padding:0;box-sizing:border-box}
html,body{width:1200px;height:813px;overflow:hidden}
body{position:relative;background:var(--page);font-family:"Source Sans 3",Arial,sans-serif;color:var(--ink)}
.abs{position:absolute}

.site-header{left:0;top:0;width:1200px;height:73px;background:var(--white)}
.logo{left:240px;top:20px;display:flex;align-items:center;gap:8px;color:var(--brand);font-size:34px;font-weight:400;letter-spacing:1px}
.logo-dot{width:26px;height:26px;border-radius:50%;background:var(--brand)}
.main-nav{left:662px;top:35px;display:flex;align-items:center;gap:18px;font-size:13px;font-weight:600}
.main-nav a{color:var(--ink);text-decoration:none}
.main-nav .current{background:var(--pill);color:var(--white);padding:3px 10px;border-radius:9px;border:1px solid #0c5f9e}

.hero{left:0;top:73px;width:1200px;height:321px;background:radial-gradient(ellipse 60% 90% at 52% 105%,#3aa7e4 0%,var(--blue) 45%,var(--blue-dark) 100%)}
.tagline{left:0;top:26px;width:1202px;text-align:center;color:var(--white);font-size:16px}
.hero-title{left:234px;top:82px;color:var(--white);line-height:1}
.hero-title .light{display:block;font-size:43px;font-weight:400}
.hero-title .bold{display:block;font-size:34px;font-weight:700;margin-top:-2px}
.hero-sub{left:234px;top:160px;color:var(--white);font-size:17px}
.join-btn{left:421px;top:203px;width:124px;height:40px;border-radius:20px;background:linear-gradient(#4fa6e2,#1b6fb7);border:1px solid #0d5494;box-shadow:0 4px 6px rgba(0,0,0,.35);color:var(--white)}
.join-btn .arrow{left:13px;top:15px;width:0;height:0;border-left:5px solid var(--white);border-top:4px solid transparent;border-bottom:4px solid transparent}
.join-btn .main{left:31px;top:7px;font-size:13px;font-weight:700}
.join-btn .small{left:31px;top:22px;font-size:9px;color:#bcdcf5}
.video-frame{left:634px;top:82px;width:325px;height:200px;background:var(--white);padding:3px;box-shadow:0 6px 6px rgba(0,0,0,.4)}
.video-slot{width:100%;height:100%;background:radial-gradient(ellipse at 50% 60%,#f2f2f2,#c9c9c9)}

.sponsors{left:0;top:394px;width:1200px;height:71px;background:linear-gradient(var(--white),var(--band));border-bottom:1px solid #d8d8d8}
.sponsors-tab{left:552px;top:-7px;width:106px;height:15px;background:var(--white);border-radius:6px 6px 0 0;text-align:center;font-size:11px;font-weight:700;line-height:15px}
.sponsor-arrow{top:29px}
.sponsor{top:22px;display:flex;align-items:center;gap:6px;font-size:20px;font-weight:600;color:#3a3a3a;transform:translateX(-50%)}
.sponsor .mark{width:22px;height:22px;border-radius:50%;background:#e0a820}
.sponsor .sq{width:20px;height:20px;background:#111}

.feature{top:495px;width:212px;height:160px}
.feature .bar{left:0;top:0;width:212px;height:4px;background:var(--rule)}
.feature h2{left:0;top:9px;font-size:19px;line-height:24px;font-weight:600;color:var(--heading);white-space:nowrap}
.feature p{left:0;top:36px;font-family:Arial,sans-serif;font-size:8.1px;line-height:13.7px;color:var(--muted);white-space:nowrap}
.feature a{left:0;top:140px;font-size:11px;line-height:14px;font-weight:600;color:#4a4a4a}

.news{left:247px;top:671px;width:698px;height:24px;border-top:1px solid #cfcfcf;border-bottom:1px solid #cfcfcf;font-size:11px;font-weight:600;color:#3a3a3a;line-height:22px}
.news .label{left:0}
.news .item{left:82px}
.news .nav{right:0}

.site-footer{left:0;top:718px;width:1200px;height:95px;background:var(--footer);color:var(--footer-text)}
.footer-nav{left:259px;top:22px;font-size:11px;font-weight:600}
.footer-rule{left:259px;top:48px;width:462px;height:1px;background:#5a5a5a}
.legal{left:259px;top:55px;font-size:9px;font-weight:600;line-height:13px}
.follow{left:798px;top:22px;font-size:14px;font-weight:600}
.social{left:798px;top:40px;display:flex;gap:7px}
.social span{width:12px;height:12px;border-radius:2px}
</style>
</head>
<body>

<header class="site-header abs">
  <div class="logo abs"><span class="logo-dot"></span>Brookvane</div>
  <nav class="main-nav abs">
    <a class="current" href="#">Home</a><a href="#">About Us</a><a href="#">Technology</a><a href="#">Press</a><a href="#">Contact Us</a>
  </nav>
</header>

<section class="hero abs">
  <p class="tagline abs">We helps advertisers understand the content and verify the context where they advertise in online video</p>
  <h1 class="hero-title abs"><span class="light">Online media</span><span class="bold">technology company</span></h1>
  <p class="hero-sub abs">Each mount bilions of video streams</p>
  <a class="join-btn abs" href="#">
    <span class="arrow abs"></span><span class="main abs">JOIN TODAY</span><span class="small abs">your future awaits</span>
  </a>
  <div class="video-frame abs"><div class="video-slot" role="img" aria-label="Company video: billions of video streams each month, with a play button"></div></div>
</section>

<section class="sponsors abs">
  <div class="sponsors-tab abs">SPONZORS</div>
  <svg class="sponsor-arrow abs" style="left:252px" width="12" height="14" viewBox="0 0 12 14"><path d="M9 1 3 7l6 6" fill="none" stroke="#1a3550" stroke-width="3"/></svg>
  <div class="sponsor abs" style="left:357px"><span class="mark"></span>Veltrion</div>
  <div class="sponsor abs" style="left:479px"><span class="sq"></span>Corvasoft</div>
  <div class="sponsor abs" style="left:614px;color:#2a6fb0">Netquill</div>
  <div class="sponsor abs" style="left:765px;color:#2a6fb0">Darrow</div>
  <div class="sponsor abs" style="left:882px"><span class="sq"></span>Helvix</div>
  <svg class="sponsor-arrow abs" style="left:945px" width="12" height="14" viewBox="0 0 12 14"><path d="M3 1l6 6-6 6" fill="none" stroke="#1a3550" stroke-width="3"/></svg>
</section>

<article class="feature abs" style="left:247px">
  <div class="bar abs"></div>
  <h2 class="abs">Video Adverstising</h2>
  <p class="abs">Everyone is talking about innovation and partner ecosys-<br>tems. What are ecosystems? They are the developers,<br>consultants, apps, integrations etc… that make your prod-<br>uct more valuable to your customers. Why do ecosystems<br>matter? Because companies like Orchard are gaining market<br>share thanks to their ecosystem. Others like<br>DealHarbor.com are retaining customers thanks to their</p>
  <a class="abs" href="#">Learn more &gt;&gt;</a>
</article>
<article class="feature abs" style="left:488px">
  <div class="bar abs"></div>
  <h2 class="abs">Pending Techonology</h2>
  <p class="abs">Everyone is talking about innovation and partner ecosys-<br>tems. What are ecosystems? They are the developers,<br>consultants, apps, integrations etc… that make your prod-<br>uct more valuable to your customers. Why do ecosystems<br>matter? Because companies like Orchard are gaining market<br>share thanks to their ecosystem. Others like<br>DealHarbor.com are retaining customers thanks to their</p>
  <a class="abs" href="#">Take a look &gt;&gt;</a>
</article>
<article class="feature abs" style="left:733px">
  <div class="bar abs"></div>
  <h2 class="abs">Video Playsment</h2>
  <p class="abs">Everyone is talking about innovation and partner ecosys-<br>tems. What are ecosystems? They are the developers,<br>consultants, apps, integrations etc… that make your prod-<br>uct more valuable to your customers. Why do ecosystems<br>matter? Because companies like Orchard are gaining market<br>share thanks to their ecosystem. Others like<br>DealHarbor.com are retaining customers thanks to their</p>
  <a class="abs" href="#">Read more &gt;&gt;</a>
</article>

<div class="news abs">
  <span class="label abs">Latest News:</span>
  <span class="item abs">January 25 , 2012 - New look at our website</span>
  <span class="nav abs">‹ ›</span>
</div>

<footer class="site-footer abs">
  <nav class="footer-nav abs">Home &nbsp;| &nbsp;About Us &nbsp;| &nbsp;Technology &nbsp;| &nbsp;Press &nbsp;| &nbsp;Contact</nav>
  <div class="footer-rule abs"></div>
  <p class="legal abs">@ 2012 Brookvane .All Rights Reserved . Various trademarks held by theirrespective owners<br>Support | Privacy | Customer Login | Blog</p>
  <div class="follow abs">Follow Us:</div>
  <div class="social abs">
    <span style="background:#3b5b9a"></span><span style="background:#3fa9e0"></span><span style="background:#e8862a"></span><span style="background:#2a77b5"></span>
  </div>
</footer>

</body>
</html>
```